Window Graphic - Restaurant Interior

We are looking to have designed a Window Graphic created to promote our dinner and pita combos in store. the graphic will be applied to the front side of our counter area glass Dimensions are 18"H x 131" LONG (FRONT) AND THE 2 SIDES ARE 18" H X 16" LONG (LEFT AND RIGHT) - SEE ATTACHED IMAGES OF THE GLASS AREA.

Our 4 Family Combos have also been attached.

PANTONE 306U (BLUE)

Target Market(s)

WOMEN AGES 18-45

Industry/Entity Type

Greek Restaurant

Font styles to use
Serif

Colors
0392cd
0455a3
33a6d7

Requirements
Must have
• Images of Food, The 4 combos, Logo (Brass Lantern)

```html
<!DOCTYPE html>
<html lang="en">
<head>
<meta charset="utf-8">
<title>Brass Lantern – Family Combos Window Graphic</title>
<link href="https://fonts.googleapis.com/css2?family=Teko:wght@400&family=Fira+Sans+Condensed:wght@400;600&family=Fira+Sans:wght@800&display=swap" rel="stylesheet">
<style>
  :root {
    --sky: #14b2e0;
    --navy: #1d3b57;
    --white: #ffffff;
    --plate: #eef1f3;
    --food-pita: #c9b28f;
    --food-dinner: #b98c52;
    --caption: #1b5f86;
  }
  * { margin: 0; padding: 0; box-sizing: border-box; }
  html, body { width: 1200px; height: 165px; overflow: hidden; background: var(--sky); }
  .banner { position: relative; width: 1200px; height: 165px; background: var(--sky); font-family: "Fira Sans Condensed", sans-serif; color: var(--navy); }

  .photo { position: absolute; }
  .title { position: absolute; top: 12px; font-family: "Teko", sans-serif; font-weight: 400; font-size: 38px; line-height: 1; text-align: right; white-space: nowrap; letter-spacing: 0; }
  .for { position: absolute; top: 43px; font-family: "Teko", sans-serif; font-weight: 400; font-size: 13px; line-height: 1; text-align: right; }
  .price { position: absolute; top: 57px; height: 37px; border-top: 1.2px dashed var(--white); border-right: 1.2px dashed var(--white); border-bottom: 1.2px dashed var(--white); color: var(--white); font-family: "Fira Sans", sans-serif; font-weight: 800; display: flex; align-items: flex-start; justify-content: flex-end; padding-right: 4px; }
  .price .cur { font-size: 13px; margin-top: 9px; margin-right: 2px; }
  .price .whole { font-size: 28px; line-height: 36px; }
  .price .cents { font-size: 13px; margin-top: 7px; margin-left: 1px; }
  .desc { position: absolute; font-weight: 600; font-size: 9px; line-height: 11px; }
  .desc--dinner { font-size: 9.5px; line-height: 12px; white-space: nowrap; }
  .note { position: absolute; top: 137px; font-weight: 400; font-size: 6.8px; color: var(--caption); white-space: nowrap; }

  .brand { position: absolute; left: 516px; top: 62px; width: 120px; text-align: center; font-family: "Teko", sans-serif; font-weight: 400; font-size: 26px; line-height: 0.95; color: var(--white); letter-spacing: 1px; }
</style>
</head>
<body>
<main class="banner">

  <!-- Pita combo for 2 -->
  <svg class="photo" style="left:28px; top:44px;" width="92" height="78" role="img" aria-label="Foil-wrapped pita sandwich on a white plate">
    <ellipse cx="46" cy="41" rx="45" ry="36" fill="var(--plate)"/>
    <ellipse cx="44" cy="36" rx="28" ry="22" fill="var(--food-pita)"/>
  </svg>
  <h2 class="title" style="right:966px;">PITA COMBO</h2>
  <span class="for" style="right:966px;">FOR 2</span>
  <div class="price" style="right:966px; width:106px;"><span class="cur">$</span><span class="whole">22</span><span class="cents">95</span></div>
  <p class="desc" style="left:34px; top:133px; width:210px;">Choice of any 2 Pita Sandwiches with choice of fries<br>or salads &amp; 2 cans of pop.</p>

  <!-- Pita combo for 4 -->
  <svg class="photo" style="left:272px; top:44px;" width="104" height="78" role="img" aria-label="Foil-wrapped pita with vegetables on a white plate">
    <ellipse cx="52" cy="41" rx="51" ry="35" fill="var(--plate)"/>
    <ellipse cx="58" cy="36" rx="30" ry="20" fill="var(--food-pita)"/>
  </svg>
  <h2 class="title" style="right:722px;">PITA COMBO</h2>
  <span class="for" style="right:722px;">FOR 4</span>
  <div class="price" style="right:722px; width:106px;"><span class="cur">$</span><span class="whole">42</span><span class="cents">95</span></div>
  <p class="desc" style="left:280px; top:133px; width:210px;">Choice of any 4 Pita Sandwiches with choice of fries<br>or salads &amp; 4 cans of pop.</p>

  <div class="brand">BRASS<br>LANTERN</div>

  <!-- Dinner combo for 2 -->
  <svg class="photo" style="left:672px; top:36px;" width="138" height="86" role="img" aria-label="Dinner plate with souvlaki, rice, greek salad, lemon potatoes and tzatziki">
    <ellipse cx="69" cy="47" rx="67" ry="38" fill="var(--plate)"/>
    <ellipse cx="72" cy="45" rx="44" ry="26" fill="var(--food-dinner)"/>
  </svg>
  <h2 class="title" style="right:298px;">DINNER COMBO</h2>
  <span class="for" style="right:298px;">FOR 2</span>
  <div class="price" style="right:298px; width:100px;"><span class="cur">$</span><span class="whole">26</span><span class="cents">95</span></div>
  <p class="desc desc--dinner" style="left:810px; top:108px;">Choice of any 2 Dinners<br>with 2 cans of pop.</p>
  <p class="note" style="left:668px;">Dinners includes greek salad, rice, lemon roasted potatoes &amp; Tzatziki.</p>

  <!-- Dinner combo for 4 -->
  <svg class="photo" style="left:924px; top:36px;" width="142" height="86" role="img" aria-label="Dinner plate with gyro meat, rice, greek salad, lemon potatoes and tzatziki">
    <ellipse cx="71" cy="47" rx="69" ry="38" fill="var(--plate)"/>
    <ellipse cx="76" cy="47" rx="44" ry="26" fill="var(--food-dinner)"/>
  </svg>
  <h2 class="title" style="right:36px;">DINNER COMBO</h2>
  <span class="for" style="right:36px;">FOR 4</span>
  <div class="price" style="right:36px; width:100px;"><span class="cur">$</span><span class="whole">52</span><span class="cents">95</span></div>
  <p class="desc desc--dinner" style="left:1070px; top:108px;">Choice of any 4 Dinners<br>with 4 cans of pop.</p>
  <p class="note" style="left:950px;">Dinners includes greek salad, rice, lemon roasted potatoes &amp; Tzatziki.</p>

</main>
</body>
</html>
```